Biz Cards for Lumivale Associates

Lumivale Associates is seeking a single-sided business card that is more visually-appealing than our current design (see attached).

Notes:
- Our colors are blue & teal.
- Our tag line must be large enough to be easily read
- We don't necessarily need our address included (that's just the biz office)
- We'd like to add our email address: Lumivale512@brindlemail.net

Thanks!

Industry/Entity Type

Business

Contact Information for Business Card

Standard size
PSD file required w/ text on its own layer

Colors
86cfc6
3277b5

```html
<!DOCTYPE html>
<html lang="en">
<head>
<meta charset="utf-8">
<title>Lumivale Associates – Business Card</title>
<link rel="stylesheet" href="https://fonts.googleapis.com/css2?family=Quicksand:wght@300;400&family=Gentium+Book+Plus:wght@400&family=PT+Sans:ital@1&display=swap">
<style>
  :root {
    --brand-blue: #3277b5;
    --brand-teal: #86cfc6;
    --ink: #1c1c1c;
    --tagline-blue: #1f68b8;
    --card-edge: #8a8a8a;
    --paper: #ffffff;
  }
  * { margin: 0; padding: 0; box-sizing: border-box; }
  html, body {
    width: 1200px; height: 1200px; overflow: hidden;
    background: var(--paper);
  }
  .card {
    position: absolute;
    left: 290px; top: 70px;
    width: 622px; height: 1062px;
    border: 1px solid var(--card-edge);
    background: var(--paper);
  }
  .card > * {
    position: absolute; left: 0; width: 100%;
    text-align: center;
  }
  .brand-mark { top: 82px; height: 140px; }
  .brand-mark svg { display: block; margin: 0 auto; }
  .brand-name {
    top: 236px;
    font-family: "Gentium Book Plus", Georgia, serif;
    font-size: 36px;
    color: var(--ink);
    letter-spacing: 1px;
    line-height: 1.2;
  }
  .person-name {
    top: 464px;
    font-family: "Quicksand", Arial, sans-serif;
    font-weight: 300;
    font-size: 47px;
    color: var(--brand-blue);
    letter-spacing: 1px;
    line-height: 1;
  }
  .person-role {
    top: 530px;
    font-family: "Gentium Book Plus", Georgia, serif;
    font-size: 31px;
    color: var(--brand-teal);
    letter-spacing: 2px;
    line-height: 1;
  }
  .contact-list {
    top: 578px;
    list-style: none;
    font-family: "Gentium Book Plus", Georgia, serif;
    font-size: 30px;
    color: var(--ink);
    letter-spacing: 2.5px;
    line-height: 51px;
  }
  .tagline {
    top: 1008px;
    font-family: "PT Sans", Arial, sans-serif;
    font-style: italic;
    font-size: 20px;
    color: var(--tagline-blue);
  }
</style>
</head>
<body>
  <main class="card">
    <div class="brand-mark">
      <svg width="170" height="140" viewBox="0 0 170 140" aria-hidden="true">
        <circle cx="85" cy="70" r="66" fill="none" stroke="var(--ink)" stroke-width="2"/>
      </svg>
    </div>
    <p class="brand-name">Lumivale Associates Ltd</p>

    <h1 class="person-name">MARISOL TREVANE, RN</h1>
    <p class="person-role">Mental Health Therapist</p>

    <ul class="contact-list">
      <li>[p] (855) 555-0142</li>
      <li>[f]&nbsp; (330) 555-0187</li>
      <li>Lumivale512@brindlemail.net</li>
      <li>Lumivale.net</li>
    </ul>

    <p class="tagline">Thoughtful Minds. Kind Hearts. Lasting Care.</p>
  </main>
</body>
</html>
```